Quellbrook Supply Chain and Logistic Consulting

Please review the attached Business Card. I want as close to this card with the colors, fonts, and quality of the card as possible. The attached compass should replace the deer head on both sides of the card and the text should say:

Backside
Compass JPEG
Quellbrook SC&L
A Supply Chain and Logistics Consulting Company

Frontside
Quellbrook SC&L
Ross Pelgrave - Tampa Florida
President
____________________________________
(555) 214-9037
QuellbrookSCL@Mailvento.com
_____________________________________

Bottom Front Side

Target Market(s)

Businesses

Contact Information for Business Card

Backside
Compass JPEG
Quellbrook SC&L

Frontside
Quellbrook SC&L
President
(555) 214-9037
QuellbrookSCL@Mailvento.com

Bottom Front Side

Font styles to use
Serif
Script

Colors

Designer to choose colors to be used in the design.

Requirements
Must have
• See attached card for reference
Nice to have
Should not have

```html
<!DOCTYPE html>
<html lang="en">
<head>
<meta charset="utf-8">
<title>Quellbrook SC&amp;L – Business Card</title>
<link href="https://fonts.googleapis.com/css2?family=Cinzel:wght@400&family=Tinos&display=swap" rel="stylesheet">
<style>
  :root {
    --backdrop: #4d4e4f;
    --card: #1c1d1f;
    --ink: #f2f2f2;
    --ink-soft: #d8d8d8;
    --rule: #9a9a9a;
    --mark: #bfbfbf;
  }
  * { margin: 0; padding: 0; box-sizing: border-box; }
  html, body {
    width: 963px; height: 1200px; overflow: hidden;
    background: var(--backdrop);
  }
  .canvas { position: relative; width: 963px; height: 1200px; }
  .card {
    position: absolute; left: 231px; width: 557px; height: 317px;
    background: var(--card);
  }
  .card--front { top: 221px; }
  .card--back { top: 636px; }

  .brand-name {
    font-family: "Tinos", serif; font-weight: 400; color: var(--ink);
    font-size: 26px; line-height: 1;
  }
  .tagline {
    font-family: "Tinos", serif; font-size: 10px; color: var(--ink-soft);
    margin-top: 6px;
  }

  .card--front .brand { position: absolute; top: 46px; right: 33px; text-align: right; }

  .holder { position: absolute; left: 33px; top: 171px; font-family: "Cinzel", serif; color: var(--ink); }
  .holder__name { font-size: 19px; letter-spacing: 0.8px; line-height: 1.1; }
  .holder__title { font-size: 12.5px; letter-spacing: 0.8px; color: var(--ink-soft); }
  .holder__rule { width: 42px; height: 1px; background: var(--rule); margin-top: 19px; }

  .contact { position: absolute; left: 33px; top: 250px; font-family: "Tinos", serif; font-size: 13px; color: var(--ink); line-height: 18px; }
  .contact__row { display: flex; gap: 29px; }

  .card--back .brand { position: absolute; left: 0; right: 0; top: 202px; text-align: center; }
  .card--back .brand-name { font-size: 29px; }
  .back-mark { position: absolute; left: 232px; top: 80px; }
</style>
</head>
<body>
<main class="canvas">
  <section class="card card--front" aria-label="Business card front">
    <div class="brand">
      <p class="brand-name">Quellbrook SC&amp;L</p>
      <p class="tagline">A Supply Chain &amp; Logistics Consulting Company</p>
    </div>
    <div class="holder">
      <p class="holder__name">Ross Pelgrave</p>
      <p class="holder__title">President</p>
      <div class="holder__rule"></div>
    </div>
    <div class="contact">
      <p>P. (555) 214-9037</p>
      <p class="contact__row"><span>QuellbrookSCL@Mailvento.com</span><span>www.quellbrookscl.com</span></p>
    </div>
  </section>

  <section class="card card--back" aria-label="Business card back">
    <svg class="back-mark" width="92" height="92" viewBox="0 0 92 92" aria-hidden="true">
      <circle cx="46" cy="46" r="44" fill="none" stroke="var(--mark)" stroke-width="2"/>
    </svg>
    <div class="brand">
      <p class="brand-name">Quellbrook SC&amp;L</p>
      <p class="tagline">A Supply Chain &amp; Logistics Consulting Company</p>
    </div>
  </section>
</main>
</body>
</html>
```